Business card for law firm

Need business card for new law firm. Think confident, authoritative, conservative, but not stuffy or old-fashioned.

Contact Information for Business Card

Content for card - logo (uploaded), plus the following:

Paul Wexbury (larger font)
Managing Partner (larger font, but not as large as name)
Level 9, 41 Tansy Lane
Sydney NSW 2000
Main Tel 02 7346 2190
Direct Tel 02 6273 4415
Email paul@qvlegal.com.au
www.qvlegal.com.au

Letterhead design should include logo plus:
Level 9, 41 Tansy Lane
Sydney NSW 2000
Tel 02 6273 4415
www.qvlegal.com.au

```html
<!DOCTYPE html>
<html lang="en">
<head>
<meta charset="utf-8">
<title>Quayvale Legal – Business Card</title>
<link href="https://fonts.googleapis.com/css2?family=EB+Garamond:wght@400;700&family=Mulish:wght@400&display=swap" rel="stylesheet">
<style>
  :root {
    --navy: #2e3a66;
    --paper: #fbfbfa;
    --ink: #3c3c3c;
    --muted: #6b6b6b;
    --rule: #b9b9b9;
    --backdrop: #d9d9d9;
  }
  html, body {
    margin: 0;
    padding: 0;
    width: 1200px;
    height: 1038px;
    overflow: hidden;
    background: var(--backdrop);
  }
  .canvas {
    position: relative;
    width: 1200px;
    height: 1038px;
  }
  .card {
    position: absolute;
    box-shadow: 0 6px 18px rgba(0,0,0,0.25);
  }
  /* Back of card */
  .card-back {
    left: 90px;
    top: 90px;
    width: 640px;
    height: 390px;
    background: var(--navy);
    color: #fff;
    display: flex;
    flex-direction: column;
    align-items: center;
    justify-content: center;
  }
  .brand-square {
    width: 96px;
    height: 96px;
    background: #fff;
    margin-bottom: 34px;
  }
  .brand-name {
    font-family: "EB Garamond", serif;
    font-weight: 400;
    font-size: 56px;
    line-height: 1;
    margin: 0 0 40px;
    color: #fff;
  }
  /* Front of card */
  .card-front {
    left: 440px;
    top: 480px;
    width: 680px;
    height: 415px;
    background: var(--paper);
    display: flex;
  }
  .front-band {
    width: 215px;
    background: var(--navy);
    display: flex;
    flex-direction: column;
    align-items: center;
    padding-top: 42px;
    box-sizing: border-box;
  }
  .band-square {
    width: 92px;
    height: 92px;
    background: #fff;
  }
  .front-details {
    padding: 58px 0 0 40px;
    font-family: "Mulish", sans-serif;
    color: var(--ink);
  }
  .person-name {
    font-family: "EB Garamond", serif;
    font-weight: 700;
    font-size: 40px;
    color: var(--navy);
    margin: 0;
    line-height: 1;
  }
  .person-title {
    font-size: 21px;
    color: var(--muted);
    margin: 6px 0 0;
  }
  .divider {
    width: 212px;
    height: 2px;
    background: var(--rule);
    margin: 18px 0 26px;
    border: 0;
  }
  .address {
    font-size: 21px;
    line-height: 1.3;
    margin: 0 0 10px;
  }
  .contact-list {
    list-style: none;
    margin: 0;
    padding: 0;
    font-size: 21px;
    line-height: 1.3;
  }
  .contact-list li {
    display: flex;
    align-items: center;
    gap: 14px;
  }
  .contact-list svg {
    width: 18px;
    height: 18px;
    flex: none;
    stroke: var(--navy);
    fill: none;
    stroke-width: 1.6;
  }
</style>
</head>
<body>
<div class="canvas">
  <section class="card card-back" aria-label="Card back">
    <div class="brand-square"></div>
    <p class="brand-name">Quayvale Legal</p>
  </section>

  <section class="card card-front" aria-label="Card front">
    <div class="front-band">
      <div class="band-square"></div>
    </div>
    <div class="front-details">
      <h1 class="person-name">Paul Wexbury</h1>
      <p class="person-title">Managing Partner</p>
      <hr class="divider">
      <p class="address">Level 9, 41 Tansy Lane<br>Sydney NSW 2000</p>
      <ul class="contact-list">
        <li><svg viewBox="0 0 20 20"><path d="M5 2 L8 6 L6 8 Q8 12 12 14 L14 12 L18 15 L16 18 Q8 18 2 6 Z"/></svg>02 7346 2190 (Main)</li>
        <li><svg viewBox="0 0 20 20"><path d="M5 2 L8 6 L6 8 Q8 12 12 14 L14 12 L18 15 L16 18 Q8 18 2 6 Z"/></svg>02 6273 4415</li>
        <li><svg viewBox="0 0 20 20"><rect x="2" y="4" width="16" height="12"/><path d="M2 4 L10 11 L18 4"/></svg>paul@qvlegal.com.au</li>
        <li><svg viewBox="0 0 20 20"><circle cx="10" cy="10" r="8"/><ellipse cx="10" cy="10" rx="3.5" ry="8"/><path d="M2 10 H18 M3.5 6 H16.5 M3.5 14 H16.5"/></svg>www.qvlegal.com.au</li>
      </ul>
    </div>
  </section>
</div>
</body>
</html>
```